International Patent Law Firm Needs a New Website Design

We are an international, German-based patent law firm and are in need for a new website design.

Our current (old-fashioned) website is

www.prtv.example

Our Corporate Identity features that we want to keep are as follows.

1. Our PRTV logo in blue color on white background.

2. The tent roof design of the Harlow Meadow Arena.

We attach our current PRTV presentation, which gives you an idea of who we are, what our business is and what distinguishes us.

The new website design should express that we provide very reliable, high-quality Intellectual Property services, including patent and trademark services worldwide.

On the one hand, it should professional, on the other it should look young.

The managing partners of our patent law firm are in their 30ies and their 40ies, which is comparably young for a patent law firm of our size. Our team comprises about 20 patent attorneys and altogether 45 people.

Websites of competitors that we like are as follows.

http://www.qzd.example
http://morwellhastings.example
http://www.dellow.example
http://www.rplaw.example (here we like the structure, rather than the design)

There are two features that all these websites have in common and that we also would like to have implemented in our new website design.

1. A clear and self-explaining main menu in the header.

For example:

HOME OUR FIRM WHAT WE DO WHO WE ARE OUR CLIENTS OUR FEES CONTACT US

2. At least on the main page: A background picture filling the entire screen and having an appealing graphic. Maybe the tent roof of the Harlow Meadow Arena?

Further points that we believe to be important are as follows:

1. Our new website should have a simple menu navigation (not as complicated as the current one). It should have two levels, namely the main page and the subpages, that are all directly accessible via the main page, so that all the content can be reached with two clicks.

2. On the WHO WE ARE subpage we like the solution that there is a list of the names of the patent attorneys in the left column, and upon clicking on a name the full profile of the patent attorney including a photograph of the partner will appear. We will have new photographs of our team prepared and supplied to you.

3. On the WHAT WE DO subpage we like the solution that there is a list of the headlines of our fields of activity, like PATENTS, and upon clicking on a headline a more detailed description of the respective field of activity will appear.

4. Our new website should contain less content than our current website. The text will be supplied by us.

5. What is also very important is that the design will be optimized for access by PCs, by tablets and by smart phones (responsive design).

6. We will need both English and German language versions of the website, including all the subpages. We will provide you with the updated text for all the pages.

Thanks very much in advance for your work and your suggestion.

Best regards,

Jonas Terholt (Partner)

Target Market(s)

Innovative and Patenting Firms worldwide, Innovators, Inventors, Potential new Employees

Industry/Entity Type

Lawyer

Number of Pages Required

5+ page

Font styles to use
Sans Serif

Colors
0555a3
0293ce

Requirements
Must have
• New appealing and modern website, self-explaining and easy menu structure
Nice to have
• Maybe some appealing design showing that we are constantly at the edge of the new technical development
Should not have
• May not look old-fashioned, no complicated menu

```html
<!DOCTYPE html>
<html lang="en">
<head>
<meta charset="utf-8">
<title>PRTV Patentanwälte</title>
<link href="https://fonts.googleapis.com/css2?family=Nunito+Sans:wght@400;600;700&display=swap" rel="stylesheet">
<style>
  :root {
    --brand-blue: #0293ce;
    --nav-grey: #7d8a96;
    --footer-grey: #a3acb4;
    --white: #ffffff;
    --hero-deep: #263f5a;
    --hero-mid: #4a6a8a;
    --hero-band: #8a9fb4;
    --hero-glow: rgba(190, 205, 220, 0.45);
    --teal-deep: #22586a;
    --teal-light: #3a7282;
    --stone: #a8a596;
    --night-deep: #272c48;
    --night-blue: #2a4b8e;
    --brick: #3a3c46;
  }
  * { margin: 0; padding: 0; box-sizing: border-box; }
  html, body {
    width: 1097px; height: 1200px; overflow: hidden;
    background: var(--white);
    font-family: "Nunito Sans", Arial, sans-serif;
  }
  .site-header {
    height: 79px; display: flex; align-items: center;
    justify-content: space-between; padding: 0 33px 0 34px;
  }
  .brand {
    color: var(--brand-blue); font-size: 30px; font-weight: 400;
    letter-spacing: 4px;
  }
  .main-nav { display: flex; gap: 20px; }
  .main-nav a {
    color: var(--nav-grey); text-decoration: none;
    font-size: 12.5px; font-weight: 400; letter-spacing: 0.2px;
  }
  .hero {
    position: relative; height: 563px; overflow: hidden; color: var(--white);
    text-align: center;
  }
  .hero-photo {
    position: absolute; inset: 0;
    background:
      radial-gradient(ellipse 70% 40% at 50% 30%, var(--hero-glow) 0%, rgba(0,0,0,0) 70%),
      linear-gradient(176deg,
        var(--hero-mid) 0%, var(--hero-deep) 12%, var(--hero-mid) 18%,
        var(--hero-band) 22%, var(--hero-mid) 27%, var(--hero-deep) 45%,
        #355574 62%, var(--hero-band) 77%, #3f5f80 83%, var(--hero-mid) 100%);
  }
  .hero-content { position: absolute; inset: 0; }
  .hero-title {
    position: absolute; top: 222px; left: 0; right: 0;
    font-size: 43px; font-weight: 700; letter-spacing: 6px; line-height: 52px;
  }
  .hero-partners {
    position: absolute; top: 326px; left: 0; right: 0;
    font-size: 15px; font-weight: 700; letter-spacing: 2.6px;
  }
  .hero-established {
    position: absolute; top: 361px; left: 0; right: 0;
    font-size: 12px; font-weight: 700; letter-spacing: 2px;
  }
  .hero-pin { position: absolute; top: 454px; left: 534px; }
  .hero-address {
    position: absolute; top: 511px; left: 0; right: 0;
    font-style: normal; font-size: 12px; font-weight: 600;
    letter-spacing: 2px; line-height: 15px;
  }
  .hero-content { top: -79px; }
  .feature-grid { display: flex; height: 505px; }
  .feature-tile {
    position: relative; flex: 1; display: flex;
    align-items: center; justify-content: center;
  }
  .feature-tile.practice {
    background:
      radial-gradient(ellipse 55% 75% at 25% 85%, var(--stone) 0%, rgba(168,165,150,0.6) 40%, rgba(0,0,0,0) 75%),
      linear-gradient(160deg, var(--teal-light) 0%, var(--teal-deep) 100%);
  }
  .feature-tile.rights {
    background:
      radial-gradient(ellipse 55% 70% at 85% 80%, var(--brick) 0%, rgba(58,60,70,0.7) 45%, rgba(0,0,0,0) 80%),
      linear-gradient(180deg, var(--night-deep) 0%, var(--night-blue) 100%);
  }
  .feature-button {
    width: 237px; height: 53px;
    border: 2px solid var(--white); color: var(--white);
    display: flex; align-items: center; justify-content: center;
    font-size: 16px; font-weight: 700; letter-spacing: 3px;
    text-decoration: none;
  }
  .site-footer {
    height: 53px; display: flex; align-items: center; padding-left: 34px;
    gap: 20px; color: var(--footer-grey);
    font-size: 11.5px; letter-spacing: 2px;
  }
</style>
</head>
<body>
  <header class="site-header">
    <div class="brand">PRTV</div>
    <nav class="main-nav">
      <a href="#">HOME</a>
      <a href="#">OUR FIRM</a>
      <a href="#">WHAT WE DO</a>
      <a href="#">WHO WE ARE</a>
      <a href="#">OUR CLIENTS</a>
      <a href="#">OUR FEES</a>
      <a href="#">CONTACT US</a>
    </nav>
  </header>

  <section class="hero">
    <div class="hero-photo" role="img" aria-label="Curved glass facade of a modern office building with reflected ceiling lights, in blue tones"></div>
    <div class="hero-content">
      <h1 class="hero-title">WELCOME TO PRTV PATENTANWÄLTE</h1>
      <p class="hero-partners">KESSLER · SANDER-NOLTE · HARTWIG</p>
      <p class="hero-established">ESTABLISHED 1985 - IN MUNICH</p>
      <svg class="hero-pin" width="28" height="40" viewBox="0 0 28 40" aria-hidden="true">
        <path d="M14 2 C7.4 2 2 7.2 2 13.6 C2 22 14 38 14 38 C14 38 26 22 26 13.6 C26 7.2 20.6 2 14 2 Z" fill="none" stroke="#fff" stroke-width="1.6"/>
        <circle cx="14" cy="13.5" r="4.5" fill="none" stroke="#fff" stroke-width="1.6"/>
      </svg>
      <address class="hero-address">
        PRTV PATENTANWÄLTE<br>
        KESSLER . SANDER - NOLTE . HARTWIG<br>
        LINDENHOFSTRASSE 42<br>
        D-80811 MÜNCHEN
      </address>
    </div>
  </section>

  <section class="feature-grid">
    <div class="feature-tile practice" role="img" aria-label="White angular building with circular perforations against a teal sky">
      <a class="feature-button" href="#">AREAS OF PRACTICE</a>
    </div>
    <div class="feature-tile rights" role="img" aria-label="Corner of a dark brick building with a cantilevered roof against a deep blue sky">
      <a class="feature-button" href="#">PROPERTY RIGHTS</a>
    </div>
  </section>

  <footer class="site-footer">
    <span>COPYRIGHT 2001-2005 PRTV ALL RIGHTS RESERVED</span>
    <span>PRTV</span>
  </footer>
</body>
</html>
```